Online Psychology Practice needs business cards.

Online Psychology service needs business cards. Have own logo- please see uploaded. I have other file formats if you need (not sure one needed?)

Details for Business Card:
Fiona Kettlewood
Clinical Psychologist BPsych, BPsych (Hons), MPsych (Clin), MAPS
T: 0457260714 | F: 08 71526804
E: hello@harbourlightmindcarestudio.com.au
W: harbourlightmindcarestudio.com.au

Industry/Entity Type

Health

Contact Information for Business Card

Logo plus details above (couldn't write in this section)

```html
<!DOCTYPE html>
<html lang="en">
<head>
<meta charset="utf-8">
<title>Harbourlight Mindcare Studio – Business Cards</title>
<link rel="stylesheet" href="https://fonts.googleapis.com/css2?family=EB+Garamond:wght@600&family=Jost:wght@400;500&display=swap">
<style>
  :root {
    --bg: #dfe4ec;
    --navy: #1a4d85;
    --navy-deep: #143f72;
    --blue-light: #2f74a8;
    --teal: #2a8cb0;
    --ink: #1d1d1f;
    --card-white: #fbfbfa;
    --white: #ffffff;
  }
  * { margin: 0; padding: 0; box-sizing: border-box; }
  html, body { width: 1200px; height: 800px; overflow: hidden; }
  body {
    background: var(--bg);
    font-family: "Jost", sans-serif;
    display: flex;
    align-items: center;
    justify-content: center;
    gap: 48px;
  }
  .card {
    width: 525px;
    height: 300px;
    border-radius: 2px;
    box-shadow: 0 18px 40px rgba(40, 60, 90, 0.18);
    position: relative;
    overflow: hidden;
  }
  .card--front {
    background: linear-gradient(150deg, var(--blue-light) 0%, var(--navy) 55%, var(--navy-deep) 100%);
    display: flex;
    align-items: center;
    justify-content: center;
  }
  .card--back {
    background: var(--card-white);
    display: flex;
    align-items: center;
    padding: 0 36px 0 40px;
  }
  .brand {
    display: flex;
    align-items: center;
    gap: 10px;
    font-family: "Jost", sans-serif;
    font-weight: 500;
    letter-spacing: 0.06em;
    text-transform: uppercase;
    line-height: 1.25;
  }
  .brand__dot {
    width: 14px;
    height: 14px;
    border-radius: 50%;
    flex: none;
  }
  .brand--light { color: var(--white); font-size: 19px; }
  .brand--light .brand__dot { background: var(--white); }
  .brand--dark { color: var(--navy); font-size: 15px; width: 200px; }
  .brand--dark .brand__dot { background: var(--navy); }
  .details { margin-left: auto; width: 250px; }
  .details__name {
    font-family: "EB Garamond", serif;
    font-weight: 600;
    font-size: 26px;
    color: var(--navy);
    line-height: 1.1;
  }
  .details__role { font-size: 14px; color: var(--teal); margin-top: 4px; }
  .details__quals { font-size: 9.5px; color: var(--ink); margin-top: 2px; }
  .details__contact { list-style: none; margin-top: 14px; font-size: 9.5px; color: var(--ink); font-weight: 500; }
  .details__contact li { margin-top: 7px; }
  .details__label { color: var(--teal); }
</style>
</head>
<body>
  <section class="card card--front" aria-label="Business card front">
    <div class="brand brand--light">
      <span class="brand__dot"></span>
      <span>Harbourlight<br>Mindcare Studio</span>
    </div>
  </section>

  <section class="card card--back" aria-label="Business card back">
    <div class="brand brand--dark">
      <span class="brand__dot"></span>
      <span>Harbourlight<br>Mindcare Studio</span>
    </div>
    <div class="details">
      <h1 class="details__name">Fiona Kettlewood</h1>
      <p class="details__role">Clinical Psychologist</p>
      <p class="details__quals">BPsych, BPsych (Hons), MPsych (Clin), MAPS</p>
      <ul class="details__contact">
        <li><span class="details__label">T:</span> 0457260714 | <span class="details__label">F:</span> 08 71526804</li>
        <li><span class="details__label">E:</span> hello@harbourlightmindcarestudio.com.au</li>
        <li><span class="details__label">W:</span> harbourlightmindcarestudio.com.au</li>
      </ul>
    </div>
  </section>
</body>
</html>
```